National Intensive Course Provider needs an advert designed to appear in trams

We need an advertisement designed to put in trams, the dimensions are 660mm wide and 203mm height. We offer intensive driving courses all over the UK, allowing pupils to complete a full driving course within a week/two weeks with both the theory and practical tests included in the course (as required). We would like the colours used to be green and dark blue, maybe red also, whatever looks best from them colours really.

Key Points to highlight:
- Pass your driving test within 1 week
- Start your course as early as next week
- Both tests included as part of your course (if required)

I have attached some images which could be included in the design

```html
<!DOCTYPE html>
<html lang="en">
<head>
<meta charset="utf-8">
<title>Rapidpass Driving – Tram Advert</title>
<link href="https://fonts.googleapis.com/css2?family=Michroma&family=Orbitron:wght@700&display=swap" rel="stylesheet">
<style>
  :root {
    --stage: #3b3b3d;
    --navy: #151a52;
    --navy-deep: #0e123d;
    --navy-soft: #1d2463;
    --red: #e0402a;
    --heading-red: #e2252b;
    --white: #ffffff;
    --silver: #c9ccd6;
    --photo-sky: #8fb4d6;
    --photo-green: #5d7f4a;
    --photo-road: #a9a39a;
  }
  * { margin: 0; padding: 0; box-sizing: border-box; }
  html, body { width: 1200px; height: 630px; overflow: hidden; }
  body { background: var(--stage); position: relative; font-family: "Michroma", sans-serif; color: var(--white); }

  .tram-banner { position: absolute; left: 55px; top: 138px; width: 1100px; height: 367px; overflow: hidden; background: var(--navy); }
  .banner-shapes { position: absolute; inset: 0; }

  .brand { position: absolute; left: 60px; top: 18px; width: 260px; text-align: center; }
  .brand-name { font-family: "Orbitron", sans-serif; font-weight: 700; font-size: 30px; letter-spacing: 2px; color: var(--white); line-height: 1.1; }
  .brand-tagline { margin-top: 8px; font-size: 10px; letter-spacing: 1.5px; line-height: 1.4; text-transform: uppercase; }

  .headline { position: absolute; left: 510px; top: 22px; font-size: 25px; color: var(--heading-red); -webkit-text-stroke: 1px var(--white); letter-spacing: 0.5px; white-space: nowrap; }

  .benefits { position: absolute; left: 632px; top: 66px; list-style: none; }
  .benefit { position: relative; padding-left: 40px; font-size: 18px; line-height: 25px; margin-bottom: 20px; text-transform: uppercase; white-space: nowrap; }
  .benefit-icon { position: absolute; left: 0; top: 3px; width: 28px; height: 20px; }

  .phone { position: absolute; left: 612px; top: 272px; display: flex; align-items: center; gap: 14px; }
  .phone-icon { width: 36px; height: 36px; }
  .phone-number { font-size: 34px; letter-spacing: 1px; white-space: nowrap; }

  .web-band { position: absolute; left: 500px; top: 325px; width: 600px; height: 42px; }
  .web-address { position: absolute; left: 572px; top: 333px; font-size: 17px; letter-spacing: 0.5px; white-space: nowrap; }
</style>
</head>
<body>
  <section class="tram-banner">
    <svg class="banner-shapes" viewBox="0 0 1100 367" width="1100" height="367" aria-hidden="true">
      <defs>
        <linearGradient id="mainPhotoTone" x1="0" y1="0" x2="0" y2="1">
          <stop offset="0" stop-color="var(--photo-sky)"/>
          <stop offset="0.45" stop-color="var(--photo-green)"/>
          <stop offset="1" stop-color="var(--photo-road)"/>
        </linearGradient>
        <linearGradient id="circlePhotoTone" x1="0" y1="0" x2="0" y2="1">
          <stop offset="0" stop-color="#4f8a4a"/>
          <stop offset="1" stop-color="#b83a3a"/>
        </linearGradient>
      </defs>
      <!-- right panel depth -->
      <polygon points="620,0 820,0 700,367 520,367" fill="var(--navy-soft)" opacity="0.55"/>
      <polygon points="880,0 1100,0 1100,120 940,367 820,367" fill="var(--navy-soft)" opacity="0.45"/>
      <!-- logo panel -->
      <polygon points="0,0 378,0 455,105 0,105" fill="var(--navy-deep)"/>
      <polygon points="378,0 392,0 470,105 455,105" fill="var(--white)"/>
      <!-- diagonal stripes -->
      <polygon points="400,0 432,0 540,367 508,367" fill="var(--silver)"/>
      <polygon points="440,0 452,0 560,367 548,367" fill="var(--white)"/>
      <polygon points="458,0 520,0 620,367 568,367" fill="var(--navy-deep)"/>
    </svg>

    <svg class="banner-shapes" viewBox="0 0 1100 367" width="1100" height="367">
      <polygon role="img" aria-label="Photo: learner driver high-fiving her instructor beside a silver L-plate car" points="0,105 450,105 520,367 0,367" fill="url(#mainPhotoTone)"/>
      <circle cx="510" cy="182" r="66" fill="var(--white)" aria-hidden="true"/>
      <circle role="img" aria-label="Photo: happy pupil holding a pass certificate next to a red car" cx="510" cy="182" r="61" fill="url(#circlePhotoTone)"/>
    </svg>

    <div class="brand">
      <div class="brand-name">RAPIDPASS</div>
      <div class="brand-tagline">Intensive Driving<br>Courses</div>
    </div>

    <h1 class="headline">INTENSIVE DRIVING COURSES</h1>

    <ul class="benefits">
      <li class="benefit">
        <svg class="benefit-icon" viewBox="0 0 28 20" aria-hidden="true"><path d="M2 10 L10 18 L26 2" fill="none" stroke="var(--white)" stroke-width="4" stroke-linecap="round" stroke-linejoin="round"/></svg>
        Pass your driving test<br>within 1 week
      </li>
      <li class="benefit">
        <svg class="benefit-icon" viewBox="0 0 28 20" aria-hidden="true"><path d="M2 10 L10 18 L26 2" fill="none" stroke="var(--white)" stroke-width="4" stroke-linecap="round" stroke-linejoin="round"/></svg>
        Start your course<br>as early as next week
      </li>
      <li class="benefit">
        <svg class="benefit-icon" viewBox="0 0 28 20" aria-hidden="true"><path d="M2 10 L10 18 L26 2" fill="none" stroke="var(--white)" stroke-width="4" stroke-linecap="round" stroke-linejoin="round"/></svg>
        Both tests included<br>as part of your course
      </li>
    </ul>

    <div class="phone">
      <svg class="phone-icon" viewBox="0 0 24 24" aria-hidden="true">
        <path d="M6.6 10.8a15.1 15.1 0 0 0 6.6 6.6l2.2-2.2a1 1 0 0 1 1-.25 11.4 11.4 0 0 0 3.6.57 1 1 0 0 1 1 1V20a1 1 0 0 1-1 1A17 17 0 0 1 3 4a1 1 0 0 1 1-1h3.5a1 1 0 0 1 1 1c0 1.25.2 2.45.57 3.6a1 1 0 0 1-.25 1z" fill="var(--white)"/>
        <path d="M15 3.5a6 6 0 0 1 5.5 5.5M15 6.5a3 3 0 0 1 2.5 2.5" fill="none" stroke="var(--white)" stroke-width="1.5" stroke-linecap="round"/>
      </svg>
      <span class="phone-number">0203 555 0184</span>
    </div>

    <svg class="web-band" viewBox="0 0 600 42" aria-hidden="true">
      <polygon points="14,0 600,0 600,42 0,42" fill="var(--red)"/>
    </svg>
    <span class="web-address">www.rapidpassdriving.co.uk</span>
  </section>
</body>
</html>
```